Harlow Reese, LLC Website

We are a small law firm in need of a website that contains the following:
1. Attractive main page
2. About us/attorney info for three people: Martin Harlow (attorney), Dean Reese (attorney), and Melissa Durant (legal assistant). We have bio's ready to submit.
3. Blog/video page. We'd like to post blogs and videos to help drive traffic
4. Multidistrict Litigation and Class Actions page, where we post information regarding active MDLs and Class actions that we are doing intake on.
Updates

Can you also please use the color "gold" in the design and logo? Thanks.

Industry/Entity Type

Legal

Coding

Coded - Design and coding required

Number of Pages Required

1 page

Colors
0054AA
0677BA
7BADD7
CADEEF
E8F1F8

Requirements
Must have
• 1. Attractive main page 2. About us/attorney info for three people: Martin Harlow (attorney), Dean Reese (attorney), and Melissa Durant (legal assistant). We have bio's ready to submit. 3. Blog/video page. We'd like to post blogs and videos to help drive traffic 4. Multidistrict Litigation and Class Actions page, where we post information regarding active MDLs and Class actions that we are doing intake on.

```html
<!DOCTYPE html>
<html lang="en">
<head>
<meta charset="utf-8">
<title>Harlow Reese, LLC — Lawyers</title>
<link href="https://fonts.googleapis.com/css2?family=Poppins:wght@300;400;500;600;700&display=swap" rel="stylesheet">
<style>
:root{
  --navy:#0b1a8e;
  --navy-deep:#07126b;
  --accent:#1a9be0;
  --gold:#c9a34a;
  --pale:#eef3fc;
  --card:#e8effb;
  --ink:#1d1d1f;
  --muted:#3c3c44;
  --white:#ffffff;
}
*{margin:0;padding:0;box-sizing:border-box}
html,body{width:1200px;height:4422px;overflow:hidden}
body{font-family:'Poppins',sans-serif;color:var(--ink);background:var(--white);position:relative}
.photo{position:absolute}
.btn{position:absolute;background:var(--navy);color:var(--white);font-size:13px;display:flex;align-items:center;justify-content:center;gap:10px;text-decoration:none}
.btn svg{width:11px;height:11px}
.section-title{position:absolute;left:0;width:1200px;text-align:center;color:var(--navy);font-weight:600;font-size:35px;letter-spacing:.5px}
.section-sub{position:absolute;left:0;width:1200px;text-align:center;font-size:13px;line-height:19px;color:var(--muted)}

/* hero */
.hero{position:absolute;left:0;top:0;width:1200px;height:670px;background:linear-gradient(120deg,#3b4149 0%,#6d6f73 30%,#2c3a5a 55%,#5b6676 80%,#2b2f38 100%)}
.hero-shade{position:absolute;inset:0;background:linear-gradient(180deg,rgba(0,0,0,.05),rgba(0,0,0,.35))}
.nav{position:absolute;left:141px;top:14px;width:918px;height:55px;background:var(--navy);color:var(--white);font-size:12px;font-weight:500;z-index:2}
.nav span{position:absolute;top:19px;white-space:nowrap}
.logo-tab{position:absolute;left:475px;top:0;width:250px;height:86px;background:var(--white);border-radius:0 0 40px 40px;z-index:3}
.brand{display:flex;align-items:center;gap:8px;color:var(--navy);font-weight:600;font-size:16px;letter-spacing:.3px;white-space:nowrap}
.brand i{display:block;width:22px;height:22px;background:var(--gold)}
.logo-tab .brand{position:absolute;left:24px;top:32px}
.hero-title{position:absolute;left:0;top:440px;width:1200px;text-align:center;color:var(--white);font-size:43px;line-height:54px;font-weight:300;z-index:2}
.hero-title b{font-weight:700}
.hero-btn{background:var(--white);color:var(--ink);left:522px;top:558px;width:156px;height:41px;z-index:2}

/* about */
.about{position:absolute;left:0;top:670px;width:1200px;height:614px;background:var(--pale)}
.about-title{position:absolute;left:664px;top:775px;font-size:24px;font-weight:400;color:var(--ink);white-space:nowrap}
.about-title b{color:var(--navy);font-size:35px;font-weight:600;margin-left:14px}
.about-text{position:absolute;left:664px;top:830px;width:390px;font-size:13.7px;line-height:21px;color:var(--muted)}
.about-text p+p{margin-top:6px}

/* team */
.member{position:absolute;top:1490px;width:282px;height:393px;text-align:center}
.member.raised{background:var(--white);box-shadow:0 4px 18px rgba(0,0,0,.12)}
.member .photo{left:24px;top:12px;width:254px;height:235px}
.member h3{position:absolute;left:0;width:100%;top:264px;font-size:15.5px;font-weight:500;letter-spacing:.3px}
.member .role{position:absolute;left:0;width:100%;top:287px;font-size:12px;font-weight:600}
.member p{position:absolute;left:22px;width:240px;top:314px;font-size:12.5px;line-height:18px;color:var(--muted)}

/* blogs */
.post{position:absolute;top:2168px;width:290px;height:410px}
.post.raised{background:var(--white);box-shadow:0 4px 18px rgba(0,0,0,.12);top:2160px;height:420px}
.post .photo{left:0;top:0;width:290px;height:204px}
.post .body{position:absolute;left:17px;top:177px;width:256px;height:213px;background:var(--card);padding:18px 17px}
.post h4{font-size:15px;font-weight:500;letter-spacing:.3px}
.post .lead{font-size:15.5px;line-height:22px;color:var(--muted);margin-top:9px;font-weight:300}
.post .text{font-size:12px;line-height:18px;color:var(--muted);margin-top:10px}
.post .more{font-size:11.5px;color:var(--navy);margin-top:10px;font-weight:500}

/* mdl */
.mdl{position:absolute;left:0;top:2742px;width:1200px;height:614px;background:var(--pale)}
.mdl-title{position:absolute;left:142px;top:2844px;font-size:35px;line-height:42px;color:var(--navy);font-weight:600}
.mdl-list{position:absolute;left:148px;top:2929px;list-style:none;font-size:14px;color:var(--muted)}
.mdl-list li{display:flex;align-items:center;gap:11px;height:35px}
.mdl-list svg{width:15px;height:15px}
.mdl-text{position:absolute;left:142px;top:3084px;width:382px;font-size:14px;line-height:21.5px;color:var(--muted)}

/* testimonials */
.quote{position:absolute;top:3566px;width:432px;height:317px;background:var(--white);border:1px solid #ececec;box-shadow:0 3px 14px rgba(0,0,0,.08);padding:45px 46px}
.quote svg{width:36px;height:30px}
.quote p{font-size:13px;line-height:25.5px;color:var(--muted);margin-top:14px}
.quote .who{font-size:12px;color:var(--accent);margin-top:14px;letter-spacing:.5px}
.arrow{position:absolute;top:3706px;width:36px;height:36px;display:flex;align-items:center;justify-content:center}
.arrow svg{width:14px;height:14px}

/* footer */
.footer{position:absolute;left:0;top:3976px;width:1200px;height:395px;background:var(--navy)}
.foot-brand{position:absolute;left:141px;top:4103px;background:var(--white);padding:7px 12px}
.foot-about{position:absolute;left:141px;top:4160px;width:285px;font-size:12.5px;line-height:23px;color:var(--white)}
.foot-col{position:absolute;top:4060px;color:var(--white)}
.foot-col h5{font-size:15px;font-weight:600;letter-spacing:.5px;margin-bottom:28px}
.links li{list-style:none;font-size:12.5px;line-height:26.6px}
.links li::before{content:"• ";color:var(--accent)}
.social{display:flex;align-items:center;gap:10px;font-size:12.5px;height:40px}
.social i{display:block;width:27px;height:27px;border:1px solid rgba(255,255,255,.7);position:relative}
.social i::after{content:"";position:absolute;left:8px;top:8px;width:9px;height:9px;border-radius:50%;background:var(--white)}
.contact{display:flex;gap:14px;font-size:12.5px;line-height:19px;margin-bottom:18px}
.contact .ic{width:28px;height:28px;border:1px solid rgba(255,255,255,.7);flex:none;display:flex;align-items:center;justify-content:center}
.contact .ic svg{width:14px;height:14px}
.contact b{font-weight:600;display:block}
.bottom{position:absolute;left:0;top:4371px;width:1200px;height:51px;background:var(--navy-deep);color:var(--white);font-size:12px;text-align:center;line-height:51px}
</style>
</head>
<body>

<!-- Hero -->
<section class="hero" role="img" aria-label="Photo of a smiling grey-bearded attorney in a suit shaking hands in an office">
  <div class="hero-shade"></div>
</section>
<nav class="nav">
  <span style="left:17px">HOME</span>
  <span style="left:91px">ABOUT US</span>
  <span style="left:192px">TEAM</span>
  <span style="left:653px">BLOG</span>
  <span style="left:726px">MDLS</span>
  <span style="left:800px">CLASS ACTIONS</span>
</nav>
<div class="logo-tab">
  <div class="brand"><i></i>HARLOW REESE LLC</div>
</div>
<h1 class="hero-title">PROTECTING YOUR RIGHTS <b>IN<br>COMPLEX LITIGATION</b></h1>
<a class="btn hero-btn">Free Consultation <svg viewBox="0 0 12 12"><path d="M2 10L10 2M4 2h6v6" stroke="#1a9be0" fill="none" stroke-width="1.3"/></svg></a>

<!-- About -->
<section class="about"></section>
<div class="photo" style="left:142px;top:831px;width:181px;height:288px;background:linear-gradient(180deg,#e6e6e8,#c9c4c0 60%,#8a5a3a 100%)" role="img" aria-label="Bronze statue of Lady Justice with scales and a gavel"></div>
<div class="photo" style="left:347px;top:757px;width:262px;height:438px;background:linear-gradient(160deg,#1b1b1e 0%,#3a3a3e 45%,#d9cdb6 60%,#2a2a2e 100%)" role="img" aria-label="Lawyer in a dark suit reading an open book"></div>
<h2 class="about-title">About<b>HARLOW REESE</b></h2>
<div class="about-text">
  <p>Lorem ipsum dolor sit amet, consectetuer adipiscing elit, sed diam nonummy nibh euismod.</p>
  <p>Lorem ipsum dolor sit amet, consectetuer adipiscing elit, sed diam nonummy nibh euismod tincidunt ut laoreet dolore magna aliquam erat volutpat. Ut wisi enim adding minim veniam, quistions nostrud exerci tation ullamcorper suscipit lobortis nisl ut aliquip exit ea commodo consequat. Duis autem vel eum iriure dolor in hendrerit in vulputate velit esse molestie consequat, vel illum dolore eu feugiat nulla facilisis at vero eros et accumsan et iusto odio dignissim qui blandit praesent luptatum zzril delenit augue duis dolore te feugait nulla facilisi.</p>
</div>
<a class="btn" style="left:664px;top:1126px;width:121px;height:43px">Read More <svg viewBox="0 0 12 12"><path d="M2 10L10 2M4 2h6v6" stroke="#1a9be0" fill="none" stroke-width="1.3"/></svg></a>

<!-- Team -->
<h2 class="section-title" style="top:1358px">OUR TEAM</h2>
<p class="section-sub" style="top:1415px">Lorem ipsum dolor sit amet, consectetuer adipiscing elit<br>sed diam nonummy nibh euismod.</p>

<div class="member" style="left:132px">
  <div class="photo" role="img" aria-label="Portrait of Martin Harlow on a blue backdrop" style="background:linear-gradient(180deg,#2d5fa0,#1f3d6e 70%,#1a1d26)"></div>
  <h3>MARTIN HARLOW</h3><div class="role">Attorney</div>
  <p>Lorem ipsum dolor sit amet, consectetuer adipiscing elit, sed diam nonummy nibh euismod.</p>
</div>
<div class="member raised" style="left:458px">
  <div class="photo" role="img" aria-label="Portrait of Dean Reese in a warmly lit office" style="left:14px;background:linear-gradient(180deg,#5a3a22,#2a1e18 60%,#15151a)"></div>
  <h3>DEAN REESE</h3><div class="role">Attorney</div>
  <p>Lorem ipsum dolor sit amet, consectetuer adipiscing elit, sed diam nonummy nibh euismod.</p>
</div>
<div class="member" style="left:767px">
  <div class="photo" role="img" aria-label="Portrait of Melissa Durant on a grey backdrop" style="background:linear-gradient(180deg,#c8c9cb,#a9abae 60%,#1e1f23)"></div>
  <h3>MELISSA DURANT</h3><div class="role">Legal Assistant</div>
  <p>Lorem ipsum dolor sit amet, consectetuer adipiscing elit, sed diam nonummy nibh euismod.</p>
</div>
<a class="btn" style="left:518px;top:1919px;width:163px;height:43px">View More Details <svg viewBox="0 0 12 12"><path d="M2 10L10 2M4 2h6v6" stroke="#1a9be0" fill="none" stroke-width="1.3"/></svg></a>

<!-- Blogs -->
<h2 class="section-title" style="top:2037px">LATEST BLOGS</h2>
<p class="section-sub" style="top:2094px">Lorem ipsum dolor sit amet, consectetuer adipiscing elit<br>sed diam nonummy nibh euismod.</p>

<article class="post" style="left:141px">
  <div class="photo" role="img" aria-label="Two professionals reviewing documents at a laptop" style="background:linear-gradient(150deg,#3a4150,#9aa3b2 50%,#e9e9ea)"></div>
  <div class="body"><h4>LOREM IPSUM DOLOR SIT.</h4><p class="lead">Lorem ipsum dolor sit amet, consectetuer adipiscing.</p><p class="text">Lorem ipsum dolor sit amet, consectetuer adipiscing elit, sed diam nonummy nibh euismod.</p><p class="more">LEARN MORE</p></div>
</article>
<article class="post raised" style="left:455px">
  <div class="photo" role="img" aria-label="Hand signing a document with a pen" style="top:8px;height:196px;background:linear-gradient(150deg,#1c2234,#5b5f6a 45%,#e4dfd5)"></div>
  <div class="body" style="top:185px"><h4>LOREM IPSUM DOLOR SIT.</h4><p class="lead">Lorem ipsum dolor sit amet, consectetuer adipiscing.</p><p class="text">Lorem ipsum dolor sit amet, consectetuer adipiscing elit, sed diam nonummy nibh euismod.</p><p class="more">LEARN MORE</p></div>
</article>
<article class="post" style="left:769px">
  <div class="photo" role="img" aria-label="Gavel, open law book and brass scales on a desk" style="background:linear-gradient(150deg,#6f7480,#b9b5ad 50%,#8a6a3a)"></div>
  <div class="body"><h4>LOREM IPSUM DOLOR SIT.</h4><p class="lead">Lorem ipsum dolor sit amet, consectetuer adipiscing.</p><p class="text">Lorem ipsum dolor sit amet, consectetuer adipiscing elit, sed diam nonummy nibh euismod.</p><p class="more">LEARN MORE</p></div>
</article>
<a class="btn" style="left:546px;top:2613px;width:106px;height:43px">View All <svg viewBox="0 0 12 12"><path d="M2 10L10 2M4 2h6v6" stroke="#1a9be0" fill="none" stroke-width="1.3"/></svg></a>

<!-- MDLs -->
<section class="mdl"></section>
<h2 class="mdl-title">MDLS AND CLASS<br>ACTIONS</h2>
<ul class="mdl-list">
  <li><svg viewBox="0 0 16 16"><circle cx="8" cy="8" r="8" fill="#1a9be0"/><path d="M6.5 4.5L10 8l-3.5 3.5" stroke="#fff" stroke-width="1.6" fill="none"/></svg>Lorem ipsum dolor sit amet</li>
  <li><svg viewBox="0 0 16 16"><circle cx="8" cy="8" r="8" fill="#1a9be0"/><path d="M6.5 4.5L10 8l-3.5 3.5" stroke="#fff" stroke-width="1.6" fill="none"/></svg>Ipsum Lorem dolor sit amet, con sectetuer</li>
  <li><svg viewBox="0 0 16 16"><circle cx="8" cy="8" r="8" fill="#1a9be0"/><path d="M6.5 4.5L10 8l-3.5 3.5" stroke="#fff" stroke-width="1.6" fill="none"/></svg>Dolor sit Lorem ipsum amet, consectet uer</li>
  <li><svg viewBox="0 0 16 16"><circle cx="8" cy="8" r="8" fill="#1a9be0"/><path d="M6.5 4.5L10 8l-3.5 3.5" stroke="#fff" stroke-width="1.6" fill="none"/></svg>Consectetuer lorem ipsum dolor sit amet</li>
</ul>
<p class="mdl-text">Lorem ipsum dolor sit amet, consectetuer adipiscing elit, sed diam nonummy nibh euismod tincidunt ut laoreet dolore magna aliquam erat volutpat. Ut wisi enim adding minim veniam, quistions nostrud exerci tation ullamcorper suscipit lobortis nisl ut aliquip exit ea commodo consequat.</p>
<a class="btn" style="left:142px;top:3226px;width:121px;height:41px">Read More <svg viewBox="0 0 12 12"><path d="M2 10L10 2M4 2h6v6" stroke="#1a9be0" fill="none" stroke-width="1.3"/></svg></a>
<div class="photo" style="left:594px;top:2831px;width:261px;height:439px;background:linear-gradient(160deg,#e9e2d6 0%,#c8a56a 35%,#5a2e1c 65%,#3a1b12 100%)" role="img" aria-label="Wooden gavel with a gold band beside brass scales"></div>
<div class="photo" style="left:879px;top:2906px;width:180px;height:290px;background:linear-gradient(170deg,#9a8f86,#eae6e0 55%,#d8d1c6)" role="img" aria-label="Hands resting on an open notebook"></div>

<!-- Testimonials -->
<h2 class="section-title" style="top:3434px">CLIENT TESTIMONIALS</h2>
<p class="section-sub" style="top:3490px">Lorem ipsum dolor sit amet, consectetuer adipiscing elit<br>sed diam nonummy nibh euismod.</p>

<div class="quote" style="left:160px">
  <svg viewBox="0 0 36 30"><path d="M2 28V17C2 8 6 3 14 1l1 3c-5 2-7 5-7 9h7v15zM21 28V17c0-9 4-14 12-16l1 3c-5 2-7 5-7 9h7v15z" fill="#0b1a8e"/></svg>
  <p>Lorem ipsum dolor sittii amet, con sectetuer there's adipiscing elitted, sed diam nonummy nibh arentoti euismod tincidunt ut laoreet dolore magna aliquam erat volutpat. Uttis wisi enim ad minim veniam, quis nostrud exerci tation ullamcorper suscipit lobortis nisl ut aliquip ex ea commodo theries is consequat.</p>
  <div class="who">- OWEN MARSH</div>
</div>
<div class="quote" style="left:615px;width:424px">
  <svg viewBox="0 0 36 30"><path d="M2 28V17C2 8 6 3 14 1l1 3c-5 2-7 5-7 9h7v15zM21 28V17c0-9 4-14 12-16l1 3c-5 2-7 5-7 9h7v15z" fill="#0b1a8e"/></svg>
  <p>Lorem ipsum dolor sittii amet, con sectetuer there's adipiscing elitted, sed diam nonummy nibh arentoti euismod tincidunt ut laoreet dolore magna aliquam erat volutpat. Uttis wisi enim ad minim veniam, quis nostrud exerci tation ullamcorper suscipit lobortis nisl ut aliquip ex ea commodo theries is consequat.</p>
  <div class="who">- CLARA BENNETT</div>
</div>
<div class="arrow" style="left:94px;background:var(--accent)"><svg viewBox="0 0 14 14"><path d="M9 2L4 7l5 5" stroke="#fff" stroke-width="2" fill="none"/></svg></div>
<div class="arrow" style="left:1069px;background:var(--navy)"><svg viewBox="0 0 14 14"><path d="M5 2l5 5-5 5" stroke="#fff" stroke-width="2" fill="none"/></svg></div>

<!-- Footer -->
<footer class="footer"></footer>
<div class="brand foot-brand"><i></i>HARLOW REESE LLC</div>
<p class="foot-about">Lorem ipsum isno dolor sitting amet, there consectetuer adipiscing elit, sedding diam nonummy nibh euismod gettes tincidunt ut laoreet dolore.</p>

<div class="foot-col" style="left:472px">
  <h5>QUICK LINKS</h5>
  <ul class="links"><li>Home</li><li>About Us</li><li>Team</li><li>Blog</li><li>MDLs</li><li>Class Actions</li><li>Contact Us</li></ul>
</div>
<div class="foot-col" style="left:644px">
  <h5>FOLLOW US</h5>
  <div class="social"><i></i>Community</div>
  <div class="social"><i></i>Updates</div>
  <div class="social"><i></i>Gallery</div>
  <div class="social"><i></i>Network</div>
</div>
<div class="foot-col" style="left:814px">
  <h5>CONTACT DETAILS</h5>
  <div class="contact"><span class="ic"><svg viewBox="0 0 14 14"><path d="M7 13S2 8 2 5a5 5 0 0110 0c0 3-5 8-5 8z" fill="none" stroke="#fff" stroke-width="1.3"/><circle cx="7" cy="5" r="1.6" fill="#fff"/></svg></span><div><b>Address</b>48, Linden Court, Elm Street<br>Fairview, State ZZ 204815</div></div>
  <div class="contact"><span class="ic"><svg viewBox="0 0 14 14"><path d="M3 1.5l2.5 2.5-1.5 1.8c.8 1.7 2 2.9 3.7 3.7L9.5 8l2.5 2.5-1.5 2C6 12.5 1.5 8 1.5 3z" fill="#fff"/></svg></span><div><b>Phone</b>(555) 014-2290</div></div>
  <div class="contact"><span class="ic"><svg viewBox="0 0 14 14"><rect x="1.5" y="3" width="11" height="8" fill="none" stroke="#fff" stroke-width="1.3"/><path d="M1.5 3L7 8l5.5-5" fill="none" stroke="#fff" stroke-width="1.3"/></svg></span><div><b>Email</b>info@harlowreese.com</div></div>
</div>
<div class="bottom">Copyright © 2025 Harlow Reese. All Rights Reserved.</div>

</body>
</html>
```